Funky Modern Flyer A5 or Postcard size

Hi, I am looking at a one small flyer (A5 or postcard size) that I can put both on my website on the front page (ie so png) and also send out if necessary.

It has to be modern, funky and hip. My brand is professional / Corporate so it also has to fit in with that brand.

There are 6 attachments:
Example 1 - FernaPeak - I like this look, clean, modern, funky and says it all.
Example 2 - FernPeak - again another look I like, simple, explanatory
Example 4 - Brightstall Bazaar - font is cool on this one but background not so much too much going on but I like the font
Example 5 - Example 4 - Brightstall Bazaar - font is cool on this one but background not so much too much going on but I like the font
5 is my logo
Example 6 is something I found on the web this morning which is effective.

It is for a Mentoring and Training program I run called: HIGHSTRIDE

What is to be included is the following:
The name: Highstride
Somewhere: Training, Mentoring
My Logo (see attached two options) you can choose which colour suits and I have the source file should you need it
My website and email: www.miriambaskell.example / miriam@miriambaskell.example

This wording: This is one of our highest in-demand programs and is based on a background and proven track record by Miriam in accelerating sales organisations and their people into stand out high performers. **(NOTE this wording in this paragraph may change and I am open to you changing if you think you can make it more effective!)

Colours: white, black and gold (those are our website colours).

I'd like the Highstride to really stand out.... I have included two fonts that I really like that I got off Brightstall Bazaar. However, feel free to suggest other fonts that you think cool or funky!
Updates

Hi everyone, just to add a note to the brief, I am not overly keen on pictures that are really busy. I only like a picture that is minimal and effective. The examples from Brightstall Bazaar was more for the Font Style not so much the pictures in the background. The pictures can take away from a design unless done really minimally.....hope this makes sense. Miriam Added Wednesday, March 15, 2017

Target Market(s)

My target Market is Corporates but I want a Funky Modern look as a lot of people in Corporates are Millennials as well which is part of my target market

Industry/Entity Type

Information Technology

Requirements
Must have
• What is to be included is the following:
• The name: Highstride
• Somewhere: Training, Mentoring
• My Logo (see attached two options) you can choose which colour suits and I have the source file should you need it
• My website and email: www.miriambaskell.example / miriam@miriambaskell.example
• This wording: This is one of our highest in-demand programs and is based on a background and proven track record in high performance and accelerating sales organisations and their people into stand out high performers. (**NOTE this wording may change when final design is picked to be changed as still working in it***)
• Colours: white, black and gold (those are our website colours).
• I'd like the Highstride to really stand out.... I have included two fonts that I really like that I got off Brightstall Bazaar. However, feel free to suggest other fonts that you think cool or funky! NOTE: The pictures I have attached is mainly for the FONTS not for the background pictures. I am not that keen on background pictures as it can take away from the font - unless it is minimal
Should not have
• Too many different colours, I like slick, modern, clean. White, gold and black preferred as this is our website colour.
• NOTE: The pictures from Brightstall Bazaar I have attached are mainly for the FONTS not for the background pictures. I am not hugely keen on background pictures as it can take away from the font/message - unless the pictures are minimal but effective.

```html
<!DOCTYPE html>
<html lang="en">
<head>
<meta charset="utf-8">
<title>Highstride – Training, Mentoring</title>
<link rel="stylesheet" href="https://fonts.googleapis.com/css2?family=Kaushan+Script&family=Lato:wght@400;700&family=Oswald:wght@700&family=Raleway:wght@400&display=swap">
<style>
  :root {
    --black: #000000;
    --white: #ffffff;
    --off-white: #f4f4f4;
    --gold: #d4a52a;
    --gold-light: #f6d36f;
    --gold-deep: #c8951d;
    --ink: #161616;
  }
  * { margin: 0; padding: 0; box-sizing: border-box; }
  html, body { width: 1200px; height: 881px; overflow: hidden; background: var(--off-white); }
  .flyer {
    position: relative;
    width: 1200px;
    height: 881px;
    background: var(--black);
    overflow: hidden;
    font-family: "Lato", sans-serif;
    color: var(--white);
  }
  .brand-mark {
    position: absolute;
    left: 225px; top: 92px;
    width: 80px; height: 80px;
    border: 3px solid var(--gold);
    border-radius: 50%;
  }
  .brand-name {
    position: absolute;
    left: 64px; top: 206px;
    font-family: "Raleway", sans-serif;
    font-weight: 400;
    font-size: 49px;
    letter-spacing: 1.5px;
    color: var(--gold);
    white-space: nowrap;
  }
  .program-title {
    position: absolute;
    left: 52px; top: 310px;
    font-family: "Kaushan Script", cursive;
    font-size: 118px;
    line-height: 1.2;
    color: var(--white);
    white-space: nowrap;
  }
  .program-services {
    position: absolute;
    left: 83px; top: 508px;
    width: 407px;
    text-align: center;
    font-family: "Kaushan Script", cursive;
    font-size: 40px;
    color: var(--gold);
    white-space: nowrap;
  }
  .services-rule {
    position: absolute;
    left: 83px; top: 569px;
    width: 407px; height: 2px;
    background: var(--white);
  }
  .program-description {
    position: absolute;
    left: 58px; top: 590px;
    width: 530px;
    font-size: 25px;
    font-weight: 700;
    line-height: 33.6px;
    letter-spacing: -0.3px;
    color: var(--white);
  }
  .headline-arc {
    position: absolute;
    left: 0; top: 0;
  }
  .headline-arc text {
    font-family: "Oswald", sans-serif;
    font-weight: 700;
    font-size: 54px;
    fill: var(--white);
  }
  .portrait {
    position: absolute;
    left: 623px; top: 155px;
    width: 478px; height: 478px;
    border-radius: 50%;
    background: radial-gradient(circle at 45% 40%, #f2f2f2 0%, #cfcfcf 45%, #5a5a5a 100%);
  }
  .region {
    position: absolute;
    left: 666px; top: 660px;
    width: 400px;
    text-align: center;
    font-size: 39px;
    font-weight: 400;
    color: var(--white);
  }
  .contact-band {
    position: absolute;
    left: 0; top: 0;
  }
  .contact-details {
    position: absolute;
    left: 575px; top: 742px;
    width: 600px;
    text-align: center;
    font-size: 35px;
    line-height: 48px;
    color: var(--ink);
  }
  .base-strip {
    position: absolute;
    left: 0; bottom: 0;
    width: 1200px; height: 33px;
    background: var(--off-white);
  }
</style>
</head>
<body>
  <main class="flyer">
    <div class="brand-mark" aria-hidden="true"></div>
    <div class="brand-name">MIRIAM BASKELL</div>

    <h1 class="program-title">Highstride</h1>
    <div class="program-services">Training, Mentoring</div>
    <div class="services-rule"></div>
    <p class="program-description">This is one of our highest in-demand programs and is based on a background and proven track record by Miriam in a sales organisations and their people into stand out high performers.</p>

    <div class="portrait" role="img" aria-label="Black and white portrait photograph of Miriam Baskell"></div>

    <svg class="headline-arc" width="1200" height="881" viewBox="0 0 1200 881" aria-label="Executive Digital Sales Strategist">
      <defs>
        <path id="title-arc" d="M 586 357 A 282 282 0 0 1 1136 357" fill="none"/>
      </defs>
      <text>
        <textPath href="#title-arc" startOffset="50%" text-anchor="middle" textLength="770" lengthAdjust="spacingAndGlyphs">EXECUTIVE DIGITAL SALES STRATEGIST</textPath>
      </text>
    </svg>

    <div class="region">Australia &amp; NZ</div>

    <svg class="contact-band" width="1200" height="881" viewBox="0 0 1200 881" aria-hidden="true">
      <defs>
        <linearGradient id="gold-sheen" x1="0" y1="0" x2="1" y2="0">
          <stop offset="0" stop-color="#c8951d"/>
          <stop offset="0.3" stop-color="#d9a62a"/>
          <stop offset="0.55" stop-color="#f6d36f"/>
          <stop offset="0.8" stop-color="#e2b53f"/>
          <stop offset="1" stop-color="#d4a52a"/>
        </linearGradient>
      </defs>
      <polygon points="563,723 1200,723 1200,848 0,848 0,767 518,767" fill="url(#gold-sheen)"/>
    </svg>

    <div class="contact-details">
      <div class="contact-email">Email: miriam@miriambaskell.example</div>
      <div class="contact-web">www.miriambaskell.example</div>
    </div>

    <div class="base-strip"></div>
  </main>
</body>
</html>
```